Take my 1-Page Consulting Service Introduction to the next level!

I am looking for a designer to enhance my current 1-Page Consulting Services Introduction.

My business - Bright Harbor Services - offers HR consulting to companies looking to be more people-centric. The design should be professional, but also convey a sense of "sparking people" or inspiring people to engage and excel.

The new Word document will:
* Use my new business logo, logo icon and colors. (files attached)
* Include my head shot (file attached)
* Impress potential clients by improving the visual appeal
* Be easy for me to update in Word (small edits)

Target Market(s)

Business owners and senior leaders

Font styles to use
Sans Serif

Requirements
Must have
• My head shot (can be cropped) , my logo
Nice to have
• use of my logo icon or parts of it (if that works for the design)

```html
<!DOCTYPE html>
<html lang="en">
<head>
<meta charset="utf-8">
<title>Bright Harbor Services – One-Page Introduction</title>
<link rel="stylesheet" href="https://fonts.googleapis.com/css2?family=Montserrat:wght@500;700;800&family=Mulish:ital,wght@0,400;0,600;1,400&family=Yellowtail&display=swap">
<style>
  :root{
    --blue:#1474c4;
    --navy:#172756;
    --white:#ffffff;
    --ink:#555a63;
    --backdrop:#666666;
    --footer:#e6e6e6;
    --photo-a:#9aa3a6;
    --photo-b:#4d5b5c;
  }
  *{box-sizing:border-box;margin:0;padding:0}
  html,body{width:1200px;height:1200px;overflow:hidden}
  body{background:var(--backdrop);font-family:"Mulish",sans-serif;position:relative}
  .sheet{position:absolute;left:271px;top:134px;width:658px;height:932px;background:var(--white);overflow:hidden}
  .sheet-shapes{position:absolute;left:0;top:0}

  .brand{position:absolute;left:36px;top:46px;color:var(--navy);font-family:"Montserrat",sans-serif;font-weight:700;font-size:27px;line-height:1.08}

  .title-pill{position:absolute;left:296px;top:30px;width:322px;height:36px;background:var(--navy);border-radius:0 18px 18px 0;color:var(--white);font-family:"Montserrat",sans-serif;font-weight:800;font-size:19px;line-height:36px;padding-left:35px;letter-spacing:.2px}
  .intro{position:absolute;left:331px;top:76px;width:292px;color:var(--white);font-size:12.7px;line-height:16px}
  .intro .profile-link{font-weight:600}

  .portrait{position:absolute;left:60px;top:203px;width:212px;height:212px;border-radius:50%;background:var(--white);box-shadow:0 3px 8px rgba(0,0,0,.25)}
  .portrait-photo{position:absolute;left:7px;top:7px;width:198px;height:198px;border-radius:50%;background:radial-gradient(circle at 50% 45%,var(--photo-a),var(--photo-b) 75%)}

  .person-name{position:absolute;left:32px;top:422px;width:271px;text-align:center;color:var(--white);font-family:"Yellowtail",cursive;font-size:33px;line-height:40px}
  .skills{position:absolute;left:68px;top:471px;list-style:none;color:var(--white);font-size:13.7px}
  .skills li{height:23.3px;line-height:18px;padding-left:22px;position:relative}
  .skills li::before{content:"";position:absolute;left:3px;top:5px;width:8px;height:8px;border-radius:50%;border:1.5px solid var(--blue)}

  .experience-title{position:absolute;left:338px;top:377px;font-family:"Montserrat",sans-serif;font-weight:800;font-size:22px;line-height:27px;color:var(--navy)}
  .experience-title span{color:var(--blue)}
  .roles{position:absolute;left:346px;top:439px;list-style:none;color:var(--ink);font-size:12px;line-height:15px}
  .roles li{position:relative;padding-left:14px;margin-bottom:6px}
  .roles li::before{content:"";position:absolute;left:0;top:4px;width:7px;height:7px;border-radius:50%;border:1.3px solid var(--blue)}
  .roles .org{color:var(--blue);font-style:italic}
  .roles .first{width:200px}
  .credentials{position:absolute;left:334px;top:642px;width:310px;color:var(--ink);font-size:12px;line-height:14.8px}

  .impact-label{position:absolute;left:32px;top:796px;width:80px;height:26px;background:var(--blue);border-radius:8px 0 0 8px;color:var(--white);font-family:"Montserrat",sans-serif;font-weight:700;font-size:13px;line-height:26px;padding-left:13px}
  .impact-card{position:absolute;top:758px;width:164px;height:104px}
  .impact-card svg{position:absolute;left:0;top:0}
  .impact-card p{position:absolute;left:17px;top:35px;width:120px;font-family:"Montserrat",sans-serif;font-weight:500;font-size:9.3px;line-height:11.3px;color:var(--navy)}
  .impact-icon{position:absolute;left:16px;top:-15px;width:42px;height:42px;border-radius:50%;background:var(--blue);border:2px solid var(--white);box-shadow:0 0 0 1.5px var(--blue)}
  .card-one{left:110px}.card-two{left:287px}.card-three{left:463px}

  .contact-bar{position:absolute;left:0;top:888px;width:658px;height:44px;background:var(--footer);border-top:1.5px solid #9a9a9a;display:flex;align-items:center;justify-content:center;color:#333;font-family:"Montserrat",sans-serif;font-weight:500;font-size:12.2px}
  .contact-bar .item{display:flex;align-items:center;gap:6px}
  .contact-bar .divider{width:1px;height:16px;background:#aaa;margin:0 22px}
</style>
</head>
<body>
<main class="sheet">
  <svg class="sheet-shapes" width="658" height="932" viewBox="0 0 658 932">
    <rect x="0" y="0" width="658" height="402" fill="var(--blue)"/>
    <path d="M0,0 H322 C300,125 215,192 0,196 Z" fill="var(--navy)"/>
    <path d="M0,0 H312 C292,110 205,172 0,176 Z" fill="var(--white)"/>
    <path d="M0,350 C40,340 120,322 200,318 C380,312 520,345 612,400 C520,356 400,324 303,326 L303,340 L0,368 Z" fill="var(--navy)"/>
    <path d="M0,362 C20,358 28,357 32,356 L32,932 H0 Z" fill="var(--white)"/>
    <path d="M303,330 C430,330 560,362 658,400 V932 H303 Z" fill="var(--white)"/>
    <path d="M32,325 H303 V697 Q303,727 273,727 H62 Q32,727 32,697 Z" fill="var(--navy)"/>
  </svg>

  <div class="brand">Bright<br>Harbor<br>Services</div>

  <h1 class="title-pill">BRIGHT HARBOR SERVICES</h1>
  <p class="intro">Dana provides people strategy expertise that enables business growth and success. She’s known for change, learning, culture and performance systems that engage and empower. Dana partners with boards and leadership teams to convert vision into action and thrives on kick-starting business initiatives. She is a champion of people-centric decision-making with a wide range of industry experience. Dana fosters cultures that create meaningful in-person, hybrid and virtual teamconnection. She has dual US and Canadian citizenship and works cross-border with ease.<span class="profile-link">www.brightharbor.example/dana</span></p>

  <div class="portrait"><div class="portrait-photo" role="img" aria-label="Head shot of Dana Whitlock"></div></div>

  <h2 class="person-name">Dana Whitlock</h2>
  <ul class="skills">
    <li>People Strategies&amp; Execution</li>
    <li>Business Transformation</li>
    <li>Change Leadership</li>
    <li>People Systems</li>
    <li>Leadership Development</li>
    <li>Personal &amp; Team Effectiveness</li>
    <li>Coaching</li>
    <li>Employee Engagement</li>
    <li>Learning &amp; Development</li>
    <li>People-Centric Outsourcing</li>
  </ul>

  <h2 class="experience-title">Professional<br><span>Experience</span></h2>
  <ul class="roles">
    <li class="first">Vice President, Development &amp; Culture | Learning <span class="org">Northwall Building Systems</span></li>
    <li>Director, Restaurant Training &amp;<br>Transformation <span class="org">Maple Grill Food Services</span></li>
    <li>Director of Education<br><span class="org">Coastal Realty Association</span></li>
    <li>Head of Virtual Communities<br><span class="org">Global Learning Council</span></li>
    <li>Director of Academic Technology Services<br><span class="org">Ridgeview College</span></li>
  </ul>
  <p class="credentials">Dana holds a Masters of Arts in Education and Human Development. She is a certified Clearview© personal effectiveness coach, a certified Pathway Assessments coach and an experienced ChangeWorks© Certified Change Practitioner.</p>

  <div class="impact-label">IMPACT</div>
  <div class="impact-card card-one">
    <svg width="164" height="104" viewBox="0 0 164 104"><path d="M8,2 H161 V18 H152 Q146,18 146,24 V80 Q146,86 152,86 H161 V102 H8 Q2,102 2,96 V8 Q2,2 8,2 Z" fill="none" stroke="var(--navy)" stroke-width="2.5"/></svg>
    <div class="impact-icon"></div>
    <p>Creating people strategies that engage, inspire and enable organizational growth and success.</p>
  </div>
  <div class="impact-card card-two">
    <svg width="164" height="104" viewBox="0 0 164 104"><path d="M8,2 H161 V18 H152 Q146,18 146,24 V80 Q146,86 152,86 H161 V102 H8 Q2,102 2,96 V8 Q2,2 8,2 Z" fill="none" stroke="var(--blue)" stroke-width="2.5"/></svg>
    <div class="impact-icon"></div>
    <p>Change leadership that is inclusive, reduces barriers and accelerates transformation.</p>
  </div>
  <div class="impact-card card-three">
    <svg width="164" height="104" viewBox="0 0 164 104"><path d="M8,2 H161 V18 H152 Q146,18 146,24 V80 Q146,86 152,86 H161 V102 H8 Q2,102 2,96 V8 Q2,2 8,2 Z" fill="none" stroke="var(--navy)" stroke-width="2.5"/></svg>
    <div class="impact-icon"></div>
    <p>Organizational development that creates highperformance and values alignment.</p>
  </div>

  <footer class="contact-bar">
    <span class="item">
      <svg width="11" height="14" viewBox="0 0 11 14"><path d="M5.5,13 C2,8.5 1,7 1,5 A4.5,4.5 0 0 1 10,5 C10,7 9,8.5 5.5,13 Z" fill="none" stroke="var(--blue)" stroke-width="1.2"/><circle cx="5.5" cy="5" r="1.6" fill="none" stroke="var(--blue)" stroke-width="1.1"/></svg>
      Port Alder, BC Canada</span>
    <span class="divider"></span>
    <span class="item">
      <svg width="13" height="13" viewBox="0 0 13 13"><path d="M3,1 L5,4 L3.8,5.4 C4.6,7.2 5.8,8.4 7.6,9.2 L9,8 L12,10 L10.6,12 C5.5,11.5 1.5,7.5 1,2.4 Z" fill="none" stroke="var(--blue)" stroke-width="1.1"/></svg>
      555.010.2471</span>
    <span class="divider"></span>
    <span class="item">
      <svg width="18" height="12" viewBox="0 0 18 12"><rect x="3" y="1" width="14" height="10" fill="none" stroke="var(--blue)" stroke-width="1.1"/><path d="M3,1 L10,7 L17,1" fill="none" stroke="var(--blue)" stroke-width="1.1"/><path d="M0,5 H2 M1,8 H2" stroke="var(--blue)" stroke-width="1"/></svg>
      dana@brightharborservices.example</span>
  </footer>
</main>
</body>
</html>
```